Business Card Design for a technology company

Our current business card is outdated and stale.

We need a new look and one soon.

We're a telematics (GPS tracking) company based in Australia. Our audiences are transport and logistics company.

Target Market(s)

1. Transport and Logistics Companies
2. Food and Beverage Manufacturers
3. Concrete Businesses

Industry/Entity Type

Logistics

Contact Information for Business Card

Halvor Pinet

Font styles to use
Sans Serif

Colors
3276b5
0255a3
85acd3
cfdeed
ffffff

Requirements
Must have
• Logo
• "Premium Suppliers of Real Time Temperature Tracking"
• Contact Name
• Business Title
• Address
• Telephone
• Mobile
• Email
• Website URL
Nice to have
• Visual representation of tracking or maps.
Should not have
• Image of a satellite as currently shown

```html
<!DOCTYPE html>
<html lang="en">
<head>
<meta charset="utf-8">
<title>Halvor Pinet — Business Card</title>
<link href="https://fonts.googleapis.com/css2?family=Roboto:wght@400;500;700&display=swap" rel="stylesheet">
<style>
  :root {
    --blue-deep: #0255a3;
    --blue-mid: #3276b5;
    --blue-light: #85acd3;
    --blue-pale: #cfdeed;
    --white: #ffffff;
    --ink: #111111;
    --stage: #e9ecef;
  }
  * { box-sizing: border-box; margin: 0; padding: 0; }
  html, body {
    width: 1200px; height: 900px; overflow: hidden;
    background: var(--stage);
    font-family: "Roboto", Arial, sans-serif;
  }
  .canvas {
    width: 1200px; height: 900px;
    display: flex; flex-direction: column; align-items: center; justify-content: center;
    gap: 30px;
  }
  .card {
    position: relative;
    width: 700px; height: 400px;
    overflow: hidden;
    box-shadow: 0 8px 24px rgba(0,0,0,.18);
  }

  /* Front */
  .card-front { background: var(--blue-deep); color: var(--white); }
  .front-brand {
    position: absolute; left: 90px; top: 120px;
    display: flex; align-items: center; gap: 16px;
  }
  .brand-dot { width: 26px; height: 26px; border-radius: 50%; background: var(--white); }
  .brand-name { font-weight: 700; font-size: 64px; letter-spacing: -1px; line-height: 1; }
  .tagline {
    position: absolute; left: 92px; top: 222px;
    font-size: 21px; font-weight: 400; letter-spacing: .2px;
  }

  /* Back */
  .card-back { background: var(--white); }
  .back-shape { position: absolute; inset: 0; }
  .back-brand {
    position: absolute; right: 56px; top: 48px;
    display: flex; align-items: center; gap: 12px;
    color: var(--blue-deep);
  }
  .back-brand .brand-dot { width: 18px; height: 18px; background: var(--blue-deep); }
  .back-brand .brand-name { font-size: 44px; }
  .contact-name {
    position: absolute; left: 48px; top: 186px;
    color: var(--blue-deep); font-size: 21px; font-weight: 500; text-transform: uppercase;
    line-height: 24px;
  }
  .contact-title {
    position: absolute; left: 48px; top: 212px;
    color: var(--ink); font-size: 17px; font-weight: 500; line-height: 20px;
  }
  .contact-list {
    position: absolute; left: 48px; top: 300px;
    list-style: none; color: var(--white); font-size: 16px;
  }
  .contact-list li { display: flex; align-items: center; gap: 10px; height: 22px; }
  .contact-list svg { width: 15px; height: 15px; fill: var(--white); flex: none; }
  .address {
    position: absolute; right: 48px; top: 210px;
    color: var(--white); font-size: 17px; line-height: 1.35; text-align: right; font-style: normal;
  }
</style>
</head>
<body>
<main class="canvas">

  <section class="card card-front" aria-label="Card front">
    <div class="front-brand">
      <span class="brand-dot"></span>
      <span class="brand-name">Halvor Pinet</span>
    </div>
    <p class="tagline">Premium Suppliers of Real Time Temperature Tracking</p>
  </section>

  <section class="card card-back" aria-label="Card back">
    <svg class="back-shape" viewBox="0 0 700 400" aria-hidden="true">
      <polygon points="0,290 700,150 700,400 0,400" fill="var(--blue-deep)"/>
      <line x1="215" y1="235" x2="700" y2="138" stroke="var(--ink)" stroke-width="2.5"/>
    </svg>

    <div class="back-brand">
      <span class="brand-dot"></span>
      <span class="brand-name">Halvor Pinet</span>
    </div>

    <h2 class="contact-name">Marla Quent</h2>
    <p class="contact-title">Managing Member</p>

    <ul class="contact-list">
      <li>
        <svg viewBox="0 0 24 24"><path d="M6.6 10.8a15 15 0 0 0 6.6 6.6l2.2-2.2a1 1 0 0 1 1-.25 11.4 11.4 0 0 0 3.6.57 1 1 0 0 1 1 1V20a1 1 0 0 1-1 1A17 17 0 0 1 3 4a1 1 0 0 1 1-1h3.5a1 1 0 0 1 1 1c0 1.25.2 2.450.57 3.57a1 1 0 0 1-.25 1z"/></svg>
        (123) 555-0148
      </li>
      <li>
        <svg viewBox="0 0 24 24"><path d="M6 2h12v5H6zM4 8h16a2 2 0 0 1 2 2v7h-4v5H6v-5H2v-7a2 2 0 0 1 2-2zm4 8v4h8v-4z"/></svg>
        (123) 555-0193
      </li>
      <li>
        <svg viewBox="0 0 24 24"><path d="M2 5h20v14H2zm2 2v.5l8 5 8-5V7zm0 2.8V17h16V9.8l-8 5z"/></svg>
        info@halvorpinet.com
      </li>
      <li>
        <svg viewBox="0 0 24 24"><path d="M12 2a10 10 0 1 0 0 20 10 10 0 0 0 0-20zm6.9 6h-2.9a15 15 0 0 0-1.4-3.6A8 8 0 0 1 18.9 8zM12 4c.8 1.2 1.5 2.5 1.9 4h-3.8c.4-1.5 1.1-2.8 1.9-4zM4.3 14a8 8 0 0 1 0-4h3.4a16 16 0 0 0 0 4zm.8 2h2.9c.3 1.3.8 2.5 1.4 3.6A8 8 0 0 1 5.1 16zM8 8H5.1a8 8 0 0 1 4.3-3.6C8.8 5.5 8.3 6.7 8 8zm4 12c-.8-1.2-1.5-2.5-1.9-4h3.8c-.4 1.5-1.1 2.8-1.9 4zm2.3-6H9.7a14.6 14.6 0 0 1 0-4h4.6a14.6 14.6 0 0 1 0 4zm.3 5.6c.6-1.1 1.1-2.3 1.4-3.6h2.9a8 8 0 0 1-4.3 3.6zm1.7-5.6a16 16 0 0 0 0-4h3.4a8 8 0 0 1 0 4z"/></svg>
        www.halvorpinet.com
      </li>
    </ul>

    <address class="address">
      4180 Corvel Ave ste 210-300<br>
      Brenton, NV 89120
    </address>
  </section>

</main>
</body>
</html>
```